BM banner

we need a banner design (36"x120" horizontal) that will be displayed on a local high school baseball field. My company ( Quill Pennant Co) has been producing signage for the Birch Meadows community since 2009. We would like to communicate that we do more than banners. The final design should include the slogan "Signs Shirts Swag" and our Logo.

Target Market(s)

companies, teams, events, shirt and other marketing items.

Industry/Entity Type

Sign, Print,

Font styles to use
Sans Serif

Requirements
Should not have
• no baseball content.

```html
<!DOCTYPE html>
<html lang="en">
<head>
<meta charset="utf-8">
<title>Quill Pennant Co – Signs Shirts Swag Banner</title>
<link rel="stylesheet" href="https://fonts.googleapis.com/css2?family=Archivo+Black&display=swap">
<style>
  :root {
    --page-bg: #e9e9e9;
    --banner-black: #141414;
    --brick-dark: #1c1c1c;
    --brick-mid: #2a2a2a;
    --frame-yellow: #b8b21e;
    --text-white: #ffffff;
    --text-cream: #fdf8d6;
    --text-yellow: #f5f032;
    --photo-dark: #1a1a1d;
    --photo-warm: #6b4a36;
  }
  * { margin: 0; padding: 0; box-sizing: border-box; }
  html, body {
    width: 1200px;
    height: 800px;
    overflow: hidden;
    background: var(--page-bg);
  }
  .banner {
    position: absolute;
    left: 0;
    top: 220px;
    width: 1200px;
    height: 360px;
    overflow: hidden;
    background:
      radial-gradient(ellipse at 70% 40%, var(--brick-mid) 0%, var(--brick-dark) 55%, var(--banner-black) 100%);
  }
  .slogan-frame {
    position: absolute;
    left: 38px;
    top: 44px;
    width: 520px;
    height: 278px;
    border: 1.5px solid var(--frame-yellow);
  }
  .slogan {
    position: absolute;
    left: 72px;
    top: 58px;
    font-family: "Archivo Black", "Arial Black", sans-serif;
    font-size: 86px;
    line-height: 0.96;
    letter-spacing: 1px;
    text-transform: uppercase;
    text-shadow: 4px 5px 6px rgba(0, 0, 0, 0.75);
  }
  .slogan span { display: block; }
  .slogan .signs { color: var(--text-white); }
  .slogan .shirts { color: var(--text-cream); }
  .slogan .swag { color: var(--text-yellow); }
  .models-photo {
    position: absolute;
    left: 520px;
    top: 36px;
    width: 520px;
    height: 324px;
    background:
      radial-gradient(ellipse at 30% 30%, var(--photo-warm) 0%, transparent 35%),
      radial-gradient(ellipse at 75% 45%, var(--photo-warm) 0%, transparent 30%),
      linear-gradient(180deg, #2b2b2e 0%, var(--photo-dark) 60%);
  }
  .brand-name {
    position: absolute;
    right: 28px;
    top: 152px;
    width: 130px;
    font-family: "Archivo Black", "Arial Black", sans-serif;
    font-size: 22px;
    line-height: 1.1;
    color: var(--text-white);
    text-align: center;
  }
</style>
</head>
<body>
  <section class="banner">
    <div class="slogan-frame"></div>
    <h1 class="slogan">
      <span class="signs">Signs</span>
      <span class="shirts">Shirts</span>
      <span class="swag">Swag</span>
    </h1>
    <div class="models-photo" role="img" aria-label="Photo of a man and a woman in sunglasses wearing dark branded pocket t-shirts against a black brick wall"></div>
    <div class="brand-name">Quill Pennant Co</div>
  </section>
</body>
</html>
```